New emergency medical service needs a marketing flyer for prospective customers

We need a tri fold brochure on an 8.5 X 11 stock for a new emergency medical service in Pennsylvania. We provide basic first aid and now Covid-19 pre screening and temperature monitoring for special events, large gatherings and businesses. Examples of these would be but not limited to: Sporting events, carnivals, festivals, craft shows, warehouses, churches, manufacturing facilities, industrial buildings, large construction sites, multi occupancy officer buildings. The market for this is pretty much untouched and endless. we would like to use gray as the back ground color and obviously our logo. The final design should grab their attention and communicate the importance of having trained and certified professionals at their event or facility. We want to give them that piece of mind they are in good hands with us.

Target Market(s)

primary focus is going to be on businesses with large offices, large buildings or lots of foot traffic in and out of the building

Requirements
Must have
• gray background, pictures, company phone # , company web site, and contact email address. I will provide all that information to the winner to add at the end.
Nice to have
• pictures that covers the whole front cover with logo at top

```html
<!DOCTYPE html>
<html lang="en">
<head>
<meta charset="utf-8">
<title>Velora Medical Services – Tri-fold Brochure</title>
<link href="https://fonts.googleapis.com/css2?family=Montserrat:wght@400;500;700;800&family=Cinzel:wght@500&display=swap" rel="stylesheet">
<style>
  :root{
    --navy:#13224f;
    --navy-deep:#0f1c45;
    --white:#ffffff;
    --paper-grey:#e9eaec;
    --page-bg:#d9dadd;
    --teal:#1bb3a0;
    --red:#c3232b;
    --ink:#1a1f33;
    --photo-teal-a:#4fa79c;
    --photo-teal-b:#2d6f74;
    --photo-lab-a:#dfe7ee;
    --photo-lab-b:#5fb6df;
    --photo-steth-a:#c9dcef;
    --photo-steth-b:#6f93bf;
    --photo-temp-a:#e4dcd6;
    --photo-temp-b:#7fb0ae;
    --map-a:#eef0ea;
    --map-b:#d7e3c9;
  }
  *{box-sizing:border-box;margin:0;padding:0}
  html,body{width:1200px;height:661px;overflow:hidden}
  body{background:var(--page-bg);font-family:'Montserrat',sans-serif;position:relative}
  .spread{position:absolute;top:114px;width:560px;height:433px;display:flex;box-shadow:0 6px 18px rgba(0,0,0,.18)}
  .spread--inside{left:30px}
  .spread--outside{left:610px}
  .panel{position:relative;width:186.67px;height:100%;overflow:hidden}
  .panel--navy{background:var(--navy);color:var(--white)}
  .panel--white{background:var(--white);color:var(--ink)}
  .panel__content{position:relative;z-index:2;padding:14px 12px 0 13px}
  .heading{font-weight:800;font-size:10.5px;letter-spacing:.2px;margin-bottom:6px;text-transform:uppercase}
  .panel--white .heading{color:var(--navy)}
  .body-copy{font-size:6.2px;line-height:1.38;text-align:justify;margin-bottom:8px}
  .panel-art{position:absolute;left:0;top:0;width:100%;height:100%;z-index:1}
  .services{display:grid;grid-template-columns:1fr 1fr;row-gap:9px;margin:8px 0 10px;text-align:center}
  .service__icon{width:32px;height:32px;border:1px solid var(--white);border-radius:50%;margin:0 auto 4px}
  .service__label{font-size:6.2px;text-transform:uppercase;letter-spacing:.2px}
  .brand{display:flex;align-items:center;gap:6px;font-weight:700;color:var(--white);font-size:15px;line-height:1.05}
  .brand__mark{width:22px;height:22px;border-radius:50%;background:var(--teal);flex:none}
  .brand--cover{color:var(--navy);justify-content:center}
  .brand--cover .brand__mark{background:var(--navy)}
  .brand-slot{position:absolute;left:0;width:100%;z-index:3;display:flex;justify-content:center}
  .map{position:absolute;left:50%;top:110px;width:152px;height:152px;margin-left:-76px;border-radius:50%;border:5px solid var(--white);background:radial-gradient(circle at 40% 40%,var(--map-a),var(--map-b));z-index:2}
  .contact{position:absolute;left:0;width:100%;top:290px;text-align:center;font-size:6.6px;line-height:1.45;z-index:2}
  .contact__icons{display:flex;justify-content:center;gap:5px;margin-bottom:4px}
  .contact__icons svg{width:10px;height:10px}
  .contact__rule{width:36px;height:1px;background:var(--white);margin:5px auto}
  .cover-title{position:absolute;left:0;width:100%;top:356px;text-align:center;font-family:'Cinzel',serif;font-weight:500;color:var(--white);font-size:12px;line-height:1.4;letter-spacing:.6px;z-index:3}
</style>
</head>
<body>

<!-- Inside spread -->
<section class="spread spread--inside">
  <article class="panel panel--navy">
    <svg class="panel-art" viewBox="0 0 187 433" preserveAspectRatio="none" aria-hidden="false">
      <path d="M0 295 L50 285 A88 88 0 0 1 140 268 L187 280 L187 433 L0 433 Z" fill="var(--paper-grey)"/>
      <defs><radialGradient id="tempShot" cx="55%" cy="45%" r="60%"><stop offset="0" stop-color="var(--photo-temp-a)"/><stop offset="1" stop-color="var(--photo-temp-b)"/></radialGradient></defs>
      <circle cx="95" cy="358" r="72" fill="url(#tempShot)" role="img" aria-label="Photo: health worker in gloves taking a masked visitor's temperature with an infrared thermometer"/>
    </svg>
    <div class="panel__content">
      <h2 class="heading">Lorem Ipsum</h2>
      <p class="body-copy">Lorem ipsum dolor sit amet, consectetuer adipiscing elit, sed diam nonummy nibh euismod tincidunt ut laoreet dolore magna aliquam erat volutpat. Ut wisi enim ad minim veniam, quis nostrud exerci tation ullamcorper suscipit lobortis nisl ut aliquip ex ea commodo consequat. Duis autem vel eum iriure dolor in hendrerit in vulputate velit esse molestie consequat, vel illum dolore eu feugiat nulla facilisis at vero eros et accumsan et iusto odio dignissim qui blandit praesent luptatum zzril delenit augue duis dolore te feugait nulla facilisi.</p>
      <p class="body-copy">Lorem ipsum dolor sit amet, cons ectetuer adipiscing elit, sed diam nonummy nibh euismod tincidunt ut laoreet dolore magna aliquam erat volutpat. Ut wisi enim ad minim veniam, quis nostrud exerci tation ullamcorper suscipit lobortis nisl ut aliquip ex ea commodo consequat.</p>
      <p class="body-copy">Lorem ipsum dolor sit amet, consectetuer adipiscing elit, sed diam nonummy nibh euismod tincidunt ut laoreet dolore magna aliquam erat volutpat. Ut wisi enim ad minim veniam, quis nostrud exerci tation ullamcorper suscipit lobortis nisl ut aliquip ex ea commodo consequat. Duis autem vel eum iriure</p>
    </div>
  </article>

  <article class="panel panel--navy">
    <div class="panel__content">
      <h2 class="heading">Services</h2>
      <p class="body-copy">Lorem ipsum dolor sit amet, consectetuer adipiscing elit, sed diam nonummy nibh euismod tincidunt ut laoreet dolore magna aliquam erat volutpat. Ut wisi enim ad minim veniam, quis nostrud exerci tation ullamcorper suscipit lobortis nisl ut aliquip ex ea commodo consequat. Duis autem vel eum iriure dolor in hendrerit in vulputate velit esse molestie consequat, vel illum dolore eu feugiat nulla facilisis at vero eros et accumsan et iusto odio dignissim qui blandit praesent luptatum zzril delenit augue duis dolore te feugait nulla facilisi</p>
      <div class="services">
        <div class="service"><div class="service__icon"></div><div class="service__label">Lorem Ipsum</div></div>
        <div class="service"><div class="service__icon"></div><div class="service__label">Lorem Ipsum</div></div>
        <div class="service"><div class="service__icon"></div><div class="service__label">Lorem Ipsum</div></div>
        <div class="service"><div class="service__icon"></div><div class="service__label">Lorem Ipsum</div></div>
        <div class="service"><div class="service__icon"></div><div class="service__label">Lorem Ipsum</div></div>
        <div class="service"><div class="service__icon"></div><div class="service__label">Lorem Ipsum</div></div>
        <div class="service"><div class="service__icon"></div><div class="service__label">Lorem Ipsum</div></div>
        <div class="service"><div class="service__icon"></div><div class="service__label">Lorem Ipsum</div></div>
      </div>
      <p class="body-copy">Lorem ipsum dolor sit amet, consectetuer adipiscing elit, sed diam nonummy nibh euismod tincidunt ut laoreet dolore magna aliquam erat volutpat. Ut wisi enim ad minim veniam, quis nostrud exerci tation ullamcorper suscipit lobortis nisl ut aliquip ex ea commodo consequat.</p>
    </div>
  </article>

  <article class="panel panel--white">
    <svg class="panel-art" viewBox="0 0 187 433" preserveAspectRatio="none">
      <defs><linearGradient id="surgeryShot" x1="0" y1="0" x2="1" y2="1"><stop offset="0" stop-color="#cfe2e0"/><stop offset=".5" stop-color="var(--photo-teal-a)"/><stop offset="1" stop-color="var(--photo-teal-b)"/></linearGradient></defs>
      <path d="M0 268 Q95 232 187 300 L187 433 L0 433 Z" fill="url(#surgeryShot)" role="img" aria-label="Photo: surgical team in teal scrubs operating under theatre lights"/>
      <path d="M0 262 Q100 222 187 292 L187 305 Q100 238 0 268 Z" fill="var(--red)"/>
    </svg>
    <div class="panel__content">
      <h2 class="heading">Lorem Ipsum</h2>
      <p class="body-copy">Lorem ipsum dolor sit amet, consectetuer adipiscing elit, sed diam nonummy nibh euismod tincidunt ut laoreet dolore magna aliquam erat volutpat. Ut wisi enim ad minim veniam, quis nostrud exerci tation ullamcorper suscipit lobortis nisl ut aliquip ex ea commodo consequat. Duis autem vel eum iriure dolor in hendrerit in vulputate velit esse molestie consequat, vel illum dolore eu feugiat nulla facilisis at vero eros et accumsan et iusto odio dignissim qui blandit praesent luptatum zzril delenit augue duis dolore te feugait nulla facilisi.</p>
      <p class="body-copy">Lorem ipsum dolor sit amet, cons ectetuer adipiscing elit, sed diam nonummy nibh euismod tincidunt ut laoreet dolore magna aliquam erat volutpat. Ut wisi enim ad minim veniam, quis nostrud exerci tation ullamcorper suscipit lobortis nisl ut aliquip ex ea commodo consequat.</p>
      <p class="body-copy">Lorem ipsum dolor sit amet, consectetuer adipiscing elit, sed diam nonummy nibh euismod tincidunt ut laoreet dolore magna aliquam erat volutpat. Ut wisi enim ad minim veniam, quis nostrud exerci tation ullamcorper suscipit lobortis</p>
    </div>
  </article>
</section>

<!-- Outside spread -->
<section class="spread spread--outside">
  <article class="panel panel--white">
    <svg class="panel-art" viewBox="0 0 187 433" preserveAspectRatio="none">
      <defs><linearGradient id="labShot" x1="0" y1="0" x2="1" y2="1"><stop offset="0" stop-color="var(--photo-lab-a)"/><stop offset=".6" stop-color="#b9cfdc"/><stop offset="1" stop-color="var(--photo-lab-b)"/></linearGradient></defs>
      <path d="M0 330 Q70 262 187 258 L187 433 L0 433 Z" fill="url(#labShot)" role="img" aria-label="Photo: lab technician in blue gloves examining a flask of blue liquid"/>
      <path d="M0 322 Q70 250 187 248 L187 258 Q70 262 0 340 Z" fill="var(--teal)"/>
    </svg>
    <div class="panel__content">
      <h2 class="heading">About Us</h2>
      <p class="body-copy">Lorem ipsum dolor sit amet, consectetuer adipiscing elit, sed diam nonummy nibh euismod tincidunt ut laoreet dolore magna aliquam erat volutpat. Ut wisi enim ad minim veniam, quis nostrud exerci tation ullamcorper suscipit lobortis nisl ut aliquip ex ea commodo consequat. Duis autem vel eum iriure dolor in hendrerit in vulputate velit esse molestie consequat, vel illum dolore eu feugiat nulla facilisis at vero eros et accumsan et iusto odio dignissim qui blandit praesent luptatum zzril delenit augue duis dolore te feugait nulla facilisi.</p>
      <p class="body-copy">Lorem ipsum dolor sit amet, cons ectetuer adipiscing elit, sed diam nonummy nibh euismod tincidunt ut laoreet dolore magna aliquam erat volutpat. Ut wisi enim ad minim veniam, quis nostrud exerci tation ullamcorper suscipit lobortis nisl ut aliquip ex ea commodo consequat.</p>
      <p class="body-copy">Lorem ipsum dolor sit amet, consectetuer adipiscing elit, sed diam nonummy nibh euismod tincidunt ut laoreet dolore magna aliquam erat volutpat. Ut wisi enim ad minim veniam, quis nostrud exerci tation ullamcorper suscipit lobortis nisl ut aliquip ex ea commodo consequat. Duis autem vel eum iriure</p>
    </div>
  </article>

  <article class="panel panel--navy">
    <div class="brand-slot" style="top:38px">
      <div class="brand"><span class="brand__mark"></span><span>Velora<br>Medical Services</span></div>
    </div>
    <div class="map" role="img" aria-label="Street map showing the service office location"></div>
    <div class="contact">
      <div class="contact__icons">
        <svg viewBox="0 0 10 10"><circle cx="5" cy="5" r="4.5" fill="none" stroke="#fff" stroke-width=".8"/><path d="M3.3 2.8 L4.2 2.6 L4.6 3.9 L4 4.3 Q4.5 5.4 5.7 6 L6.1 5.4 L7.3 5.8 L7.2 6.7 Q4 7 3.3 2.8 Z" fill="#fff"/></svg>
        <svg viewBox="0 0 10 10"><circle cx="5" cy="5" r="4.5" fill="none" stroke="#fff" stroke-width=".8"/><rect x="2.8" y="3.4" width="4.4" height="3.2" fill="none" stroke="#fff" stroke-width=".6"/><path d="M2.8 3.4 L5 5.2 L7.2 3.4" fill="none" stroke="#fff" stroke-width=".6"/></svg>
        <svg viewBox="0 0 10 10"><circle cx="5" cy="5" r="4.5" fill="none" stroke="#fff" stroke-width=".8"/><circle cx="5" cy="5" r="2.6" fill="none" stroke="#fff" stroke-width=".5"/><ellipse cx="5" cy="5" rx="1.1" ry="2.6" fill="none" stroke="#fff" stroke-width=".5"/><path d="M2.4 5 H7.6" stroke="#fff" stroke-width=".5"/></svg>
      </div>
      <div>+0 123 456 789</div>
      <div>info@yourmail.com</div>
      <div>www.yourcompany.com</div>
      <div class="contact__rule"></div>
      <div>Your address, Suit # 000,<br>Dummy Street, City, State,</div>
    </div>
  </article>

  <article class="panel panel--white">
    <svg class="panel-art" viewBox="0 0 187 433" preserveAspectRatio="none">
      <defs><linearGradient id="stethShot" x1="0" y1="0" x2="1" y2="1"><stop offset="0" stop-color="var(--photo-steth-a)"/><stop offset="1" stop-color="var(--photo-steth-b)"/></linearGradient></defs>
      <path d="M0 0 H187 V195 Q120 260 0 258 Z" fill="url(#stethShot)" role="img" aria-label="Photo: stethoscope resting on an ECG chart"/>
      <path d="M0 258 Q120 260 187 195 L187 210 Q120 272 0 266 Z" fill="var(--teal)"/>
      <path d="M0 345 L187 335 L187 433 L0 433 Z" fill="var(--navy)"/>
    </svg>
    <div class="brand-slot" style="top:282px">
      <div class="brand brand--cover"><span class="brand__mark"></span><span>Velora<br>Medical Services</span></div>
    </div>
    <div class="cover-title">Lorem Ipsum<br>Dolor Sit Amet</div>
  </article>
</section>

</body>
</html>
```